Single Page Digital Brochure

We are a Sydney based finance company. We lend money to developers. Please see attached example of what we are looking to have produced. We just need a design which can be posted on LINKEDIN

Target Market(s)

Property Developers who are borrowing money

Industry/Entity Type

Finance

Requirements
Must have
• Australian relevant imagery.

TEXT TO INCLUDE:

New Offering from Ferngate Lending
Nice to have
• Design and colour scheme based around our logo (attached)

Please include the same text as the attachment

Please make the design based loosely on the attachment. But do not copy the attachement
Should not have
• Remove Text: 'Settle in under four days'

```html
<!DOCTYPE html>
<html lang="en">
<head>
<meta charset="utf-8">
<title>Ferngate Lending – New Offering</title>
<link rel="stylesheet" href="https://fonts.googleapis.com/css2?family=Oswald:wght@300;600&family=Montserrat:wght@400;600;700&display=swap">
<style>
  :root {
    --page-bg: #e8e8e8;
    --paper: #efefef;
    --green: #234f38;
    --ink: #1f1f1f;
    --footer: #2a2a2a;
    --white: #ffffff;
  }
  * { margin: 0; padding: 0; box-sizing: border-box; }
  html, body {
    width: 774px; height: 1200px; overflow: hidden;
    background: var(--page-bg);
  }
  .brochure {
    position: absolute; left: 37px; top: 353px;
    width: 700px; height: 494px;
    background: var(--paper);
    box-shadow: 0 4px 14px rgba(0,0,0,0.18);
    overflow: hidden;
    font-family: "Montserrat", Arial, sans-serif;
  }
  .panel-art { position: absolute; left: 0; top: 0; width: 700px; height: 432px; }

  .brand {
    position: absolute; left: 42px; top: 108px;
    display: flex; align-items: center; gap: 8px;
    color: var(--green);
    font-weight: 600; font-size: 17px; letter-spacing: 0.5px;
  }
  .brand-dot { width: 14px; height: 14px; border-radius: 50%; background: var(--green); }

  .headline {
    position: absolute; left: 41px; top: 164px;
    font-family: "Oswald", "Arial Narrow", sans-serif;
    color: var(--green);
    font-size: 46px; line-height: 47px; text-transform: uppercase;
    letter-spacing: -0.5px;
  }
  .headline .strong { font-weight: 600; display: block; }
  .headline .light { font-weight: 300; display: block; color: var(--ink); }

  .divider { position: absolute; left: 42px; top: 315px; width: 87px; height: 1px; background: var(--ink); }
  .divider::after {
    content: ""; position: absolute; left: 19px; top: -1.5px;
    width: 25px; height: 4px; border-radius: 2px; background: var(--green);
  }

  .services {
    position: absolute; left: 42px; top: 355px; width: 245px;
    font-size: 8.2px; font-weight: 600; line-height: 11.7px; color: var(--ink);
  }

  .result-title {
    position: absolute; left: 405px; top: 70px;
    font-family: "Oswald", "Arial Narrow", sans-serif;
    color: var(--white); text-transform: uppercase;
  }
  .result-title .strong { display: block; font-weight: 600; font-size: 40px; line-height: 42px; }
  .result-title .light { display: block; font-weight: 300; font-size: 30px; line-height: 34px; letter-spacing: -0.3px; }
  .result-rule { position: absolute; left: 406px; top: 150px; width: 55px; height: 2px; background: var(--white); }

  .deal-terms { position: absolute; left: 406px; top: 175px; list-style: none; color: var(--white); font-size: 10.3px; }
  .deal-terms li { position: absolute; left: 0; white-space: nowrap; }
  .deal-terms .label { font-weight: 700; letter-spacing: 0.4px; margin-right: 8px; }
  .deal-terms .value { font-weight: 400; }

  .contact-bar {
    position: absolute; left: 0; top: 432px; width: 700px; height: 62px;
    background: var(--footer); color: var(--white);
    display: flex; align-items: center; padding-left: 41px;
    font-size: 18.5px; font-weight: 400; white-space: nowrap;
  }
  .contact-bar .phone { font-weight: 700; margin-left: 6px; letter-spacing: 0.5px; }
  .contact-bar .sep { margin: 0 28px 0 24px; font-weight: 600; }
  .contact-bar .web { display: flex; align-items: center; gap: 9px; }
</style>
</head>
<body>
  <main class="brochure">
    <svg class="panel-art" viewBox="0 0 700 432">
      <defs>
        <linearGradient id="harbourGrey" x1="0" y1="0" x2="0" y2="1">
          <stop offset="0" stop-color="#f3f3f3"/>
          <stop offset="0.28" stop-color="#e9e9e9"/>
          <stop offset="0.42" stop-color="#d6d6d6"/>
          <stop offset="0.62" stop-color="#dedede"/>
          <stop offset="0.78" stop-color="#e4e4e4"/>
          <stop offset="1" stop-color="#d2d2d2"/>
        </linearGradient>
        <linearGradient id="skylineGreen" x1="0" y1="0" x2="0" y2="1">
          <stop offset="0" stop-color="#235239"/>
          <stop offset="0.35" stop-color="#1f4a34"/>
          <stop offset="0.6" stop-color="#2a5a40"/>
          <stop offset="0.75" stop-color="#1b4230"/>
          <stop offset="1" stop-color="#143226"/>
        </linearGradient>
      </defs>
      <polygon role="img" aria-label="Faded grey photograph of the Sydney Harbour Bridge and city skyline"
               points="0,0 384,0 311,432 0,432" fill="url(#harbourGrey)"/>
      <polygon points="384,0 393,0 320,432 311,432" fill="#ffffff"/>
      <polygon role="img" aria-label="Green tinted photograph of the Sydney skyline with Sydney Tower over the harbour"
               points="393,0 700,0 700,432 320,432" fill="url(#skylineGreen)"/>
      <polyline points="29,432 29,33 378,33" fill="none" stroke="#2a3a30" stroke-width="1"/>
      <polyline points="388,33 667,33 667,432" fill="none" stroke="rgba(255,255,255,0.75)" stroke-width="1"/>
    </svg>

    <div class="brand"><span class="brand-dot"></span>Ferngate Lending</div>

    <h1 class="headline">
      <span class="strong">New Offering</span>
      <span class="strong">From Ferngate</span>
      <span class="light">Lending</span>
    </h1>
    <div class="divider"></div>
    <p class="services">Factor Financing, Accounts Receivable Financing, Pur-chase Order Financing, Contract Financing, Construction Financing, and Business Financing Attainment</p>

    <h2 class="result-title">
      <span class="strong">We Did</span>
      <span class="light">Just Last Week.</span>
    </h2>
    <div class="result-rule"></div>

    <ul class="deal-terms">
      <li style="top:0"><span class="label">LONE AMOUNT :</span><span class="value">$750.000</span></li>
      <li style="top:28px"><span class="label">RATE :</span><span class="value">7.79%</span></li>
      <li style="top:56px"><span class="label">TERM :</span><span class="value">12 Months</span></li>
      <li style="top:85px"><span class="label">LVR :</span><span class="value">60%</span></li>
      <li style="top:114px"><span class="label">REPAYMENTS :</span><span class="value">Capitalsod</span></li>
      <li style="top:144px"><span class="label">SECURITY :</span><span class="value">2x sydncy Residential Properties</span></li>
      <li style="top:174px"><span class="label">PURPOSE :</span><span class="value">Business Working Capital</span></li>
    </ul>

    <footer class="contact-bar">
      <span>call Mia today on</span><span class="phone">1300 555 014</span>
      <span class="sep">|</span>
      <span class="web">
        <svg width="16" height="16" viewBox="0 0 16 16" aria-hidden="true">
          <g fill="none" stroke="#ffffff" stroke-width="1.3">
            <circle cx="8" cy="8" r="6.8"/>
            <ellipse cx="8" cy="8" rx="3" ry="6.8"/>
            <line x1="1.2" y1="8" x2="14.8" y2="8"/>
            <line x1="2.2" y1="4.5" x2="13.8" y2="4.5"/>
            <line x1="2.2" y1="11.5" x2="13.8" y2="11.5"/>
          </g>
        </svg>
        ferngatelending.com
      </span>
    </footer>
  </main>
</body>
</html>
```